Stonebridge 720 Real Estate Investment Company

We need a business card designed for a real estate investment company named Stonebridge 720. We want to use red#f04a50, orange #f37122 and yellow #fbee3e as the color scheme. The logo colors will need to be modified from the current blue palette. I've attach VitalBranchly logo example that captures the color scheme we're going for for Stonebridge 720. Looking for clean Sans Serif fonts.
Contact Information for Business Card
Daniel Whitlock
Managing Partner
48613 Kessler Lane, Suite 540
Tampa, FL 33671
813-555-8740 Mobile
dwhitlock@stonebridge720.example
www.stonebridge720.example
Requirements
Must have
- Looking for creative responses.
Nice to have
- Must hit color palette... orange, red, yellow

```html
<!DOCTYPE html>
<html lang="en">
<head>
<meta charset="utf-8">
<title>Stonebridge 720 – Business Card</title>
<link rel="stylesheet" href="https://fonts.googleapis.com/css2?family=Oswald:wght@500;600&family=Lato:wght@400;700&display=swap">
<style>
  :root {
    --red: #f04a50;
    --deep-red: #e8222a;
    --orange: #f37122;
    --yellow: #fbee3e;
    --ink: #2b2b2b;
    --rule: #c9c9c9;
    --paper: #fbfbfa;
    --backdrop: #2e2a29;
  }
  * { margin: 0; padding: 0; box-sizing: border-box; }
  html, body {
    width: 1200px; height: 844px; overflow: hidden;
    background: var(--backdrop);
  }
  .canvas {
    position: relative; width: 1200px; height: 844px;
    display: flex; align-items: center; justify-content: center; gap: 40px;
  }
  .card {
    position: relative; width: 540px; height: 308px;
    border-radius: 3px; overflow: hidden;
    box-shadow: 0 10px 28px rgba(0,0,0,.45);
  }

  /* Front: contact side */
  .card-front { background: var(--paper); font-family: "Lato", sans-serif; color: var(--ink); }
  .brand {
    position: absolute; right: 44px; top: 46px;
    display: flex; align-items: center; gap: 10px;
  }
  .brand-name {
    font-family: "Oswald", sans-serif; font-weight: 600;
    font-size: 30px; letter-spacing: .2px; color: var(--orange);
  }
  .brand-dot { width: 14px; height: 14px; border-radius: 50%; background: var(--red); }
  .rule { position: absolute; left: 40px; right: 40px; height: 1px; background: var(--rule); }
  .rule-top { top: 102px; }
  .rule-mid { top: 146px; }
  .rule-short { top: 268px; right: 260px; }
  .contact { position: absolute; left: 40px; bottom: 46px; }
  .person-name {
    font-family: "Oswald", sans-serif; font-weight: 500;
    font-size: 22px; color: var(--orange); line-height: 1.05;
  }
  .person-title { font-size: 14px; line-height: 1.3; margin-bottom: 6px; }
  .contact-line { font-size: 14px; line-height: 1.5; }
  .label { color: var(--orange); }
  .web-www { color: var(--orange); }
  .web-name { color: var(--red); }
  .web-tld { color: #e9d21e; }
  .address { position: absolute; left: 40px; bottom: 14px; font-size: 15px; }

  /* Back: brand side */
  .card-back {
    background: linear-gradient(200deg, var(--yellow) 0%, #f7a21f 22%, var(--deep-red) 52%, var(--deep-red) 62%, var(--orange) 100%);
    display: flex; align-items: center; justify-content: center;
  }
  .back-pattern { position: absolute; inset: 0; background: radial-gradient(ellipse at 50% 40%, rgba(255,255,255,.06), rgba(255,255,255,0) 70%); }
  .back-brand { position: relative; display: flex; align-items: center; gap: 12px; }
  .back-brand .brand-name { color: #fff; font-size: 36px; }
  .back-brand .brand-dot { background: #fff; width: 16px; height: 16px; }
</style>
</head>
<body>
  <main class="canvas">
    <section class="card card-front" aria-label="Business card, contact side">
      <div class="brand">
        <span class="brand-name">Stonebridge720</span>
        <span class="brand-dot"></span>
      </div>
      <div class="rule rule-top"></div>
      <div class="rule rule-mid"></div>
      <div class="contact">
        <p class="person-name">Daniel Whitlock</p>
        <p class="person-title">Managing Partner</p>
        <p class="contact-line"><span class="label">P:</span> 813-555-8740 | <span class="label">E:</span> dwhitlock@stonebridge720.example</p>
        <p class="contact-line"><span class="web-www">www.</span><span class="web-name">stonebridge720</span><span class="web-tld">.example</span></p>
      </div>
      <div class="rule rule-short"></div>
      <p class="address">48613 Kessler Lane, Suite 540 Tampa, FL 33671</p>
    </section>

    <section class="card card-back" aria-label="Business card, brand side">
      <div class="back-pattern" role="img" aria-label="Faint repeating brand-mark pattern over a yellow to red to orange gradient"></div>
      <div class="back-brand">
        <span class="brand-name">Stonebridge720</span>
        <span class="brand-dot"></span>
      </div>
    </section>
  </main>
</body>
</html>
```